Redesign retirement planner website

Provide an original design for a website. The site should introduce the retirement planner, explain the basic offerings of his services, and invite the website visitor to enter their name, phone, and email. Please provide a ready-to-publish redesign that can actually be published via a Wordpress template or other major website builder like SquareSpace or Wix. Some introductory content is attached, but feel free to add additional sections/images/blocks/copywriting and rearrange/delete sections entirely to make your design original and compelling. Feel free to pull copywriting from here but again, do not use this original design, feel free to create an entirely NEW design and layout. lynx-mango-trel (dot) sitefolio (dot) com password: 1234 -- FINAL NOTE: Do not choose a stock photo of a man for the retirement planner. This website needs to work well with no photo of the retirement planner himself. Think of a non-face-focused design to win this competition.

Industry/Entity Type

Retirement planner personal website

Number of Pages Required

1 page

Font styles to use
Sans Serif
Decorative

Requirements
Must have
• Please provide a ready-to-publish redesign that can actually be published via a Wordpress template or other major website builder.

```html
<!DOCTYPE html>
<html lang="en">
<head>
<meta charset="UTF-8">
<title>Dalton Whitfield — Counselor &amp; Retirement Specialist</title>
<link href="https://fonts.googleapis.com/css2?family=Lato:wght@400;700;900&display=swap" rel="stylesheet">
<style>
:root{
  --gold:#ffc700;
  --gold-deep:#f5bd00;
  --gold-soft:#fdf6e0;
  --ink:#0d0d0d;
  --muted:#555;
  --field:#ebebeb;
  --white:#fff;
  --line:#e2e2e2;
}
*{box-sizing:border-box;margin:0;padding:0}
html,body{width:1200px;height:2785px;overflow:hidden;background:var(--white)}
body{font-family:'Lato',sans-serif;color:var(--ink)}
.page{position:relative;width:1200px;height:2785px;overflow:hidden}
.abs{position:absolute}

/* header */
.brand{left:111px;top:16px;font-size:43px;font-weight:700;letter-spacing:-.5px}
.nav{left:525px;top:26px;display:flex;align-items:center;font-size:16px}
.nav a{color:var(--ink);text-decoration:none}
.nav .active{background:var(--gold);font-weight:700;padding:5px 14px;border-radius:2px}
.nav .n2{margin-left:70px}.nav .n3{margin-left:83px}
.nav .cta{margin-left:36px;background:var(--gold);font-weight:700;padding:10px 19px;border-radius:3px}

/* hero */
.hero{left:0;top:86px;width:1200px;height:600px;border-radius:0 0 55px 55px;
  background:linear-gradient(120deg,#d9d3c6 0%,#b9ad98 30%,#8d7e6a 55%,#c8c3bb 80%,#e7e4df 100%)}
.hero-box{left:220px;top:312px;width:762px;height:251px;background:rgba(255,199,0,.9);border-radius:6px;text-align:center}
.hero-box h1{font-size:70px;font-weight:700;line-height:78px;margin-top:20px;letter-spacing:-.5px}
.hero-box p{font-size:27px;margin-top:8px}

/* section titles */
.title{font-size:45px;font-weight:700;letter-spacing:-.3px}
.title span{color:var(--gold)}

/* specialties */
.card{top:843px;width:227px;height:219px;border:2px solid var(--line);border-radius:14px;background:var(--white);padding:22px 20px;box-shadow:0 2px 6px rgba(0,0,0,.06)}
.card.on{background:var(--gold);border-color:var(--gold)}
.card .ico{width:62px;height:62px;border-radius:8px;background:var(--gold-soft);display:flex;align-items:center;justify-content:center}
.card.on .ico{background:var(--ink)}
.card h3{margin-top:14px;font-size:19px;font-weight:700;border-left:2px solid var(--gold);padding-left:10px;line-height:20px}
.card.on h3{border-color:var(--ink)}
.card p{margin-top:14px;font-size:13.5px;line-height:20.5px;color:var(--muted)}
.card.on p{color:var(--ink)}
.arrow{top:936px;width:31px;height:31px;border-radius:50%;background:var(--ink);display:flex;align-items:center;justify-content:center}

/* quote band */
.quote{left:111px;top:1147px;width:977px;height:330px;border-radius:26px;
  background:linear-gradient(100deg,#f7c400 0%,#f0c20c 50%,#e6b400 100%);
  display:flex;align-items:center;justify-content:center;text-align:center;padding:0 60px}
.quote p{font-size:30px;font-weight:700;line-height:39.5px}

/* offerings */
.offer{top:1640px;width:250px;height:213px;text-align:center;border-radius:6px}
.offer.on{background:var(--gold-soft)}
.offer h4{font-size:24px;font-weight:700;line-height:29px}

/* form */
.sub{font-size:26px;color:#333;text-align:center;width:1200px;left:0}
.field{background:var(--field);border-radius:3px;font-size:15px;color:#666;padding:22px 21px}
.btn{left:540px;top:2254px;width:120px;height:38px;background:var(--gold);border-radius:3px;font-size:15px;font-weight:700;display:flex;align-items:center;justify-content:center}

/* footer */
.footer{left:0;top:2378px;width:1200px;height:380px;background:var(--ink);border-radius:60px 60px 0 0}
.foot-brand{width:1200px;left:0;top:2480px;text-align:center;font-size:52px;font-weight:700;color:var(--gold)}
.foot-nav{left:0;top:2562px;width:1200px;color:var(--white);font-size:16px}
.foot-nav span{position:absolute}
.social{top:2625px;width:32px;height:32px;border-radius:4px}
.bar{left:0;top:2738px;width:1200px;height:47px;background:var(--gold);text-align:center;font-size:14px;line-height:47px}
</style>
</head>
<body>
<div class="page">

  <div class="abs brand">Dalton Whitfield</div>
  <nav class="abs nav">
    <a class="active" href="#">Home</a>
    <a class="n2" href="#">Specialties</a>
    <a class="n3" href="#">Insurance Offers</a>
    <a class="cta" href="#">Contact Me</a>
  </nav>

  <div class="abs hero" role="img" aria-label="Photo of an older couple reviewing retirement documents with an advisor in a bright living room"></div>
  <div class="abs hero-box">
    <h1>Counselor &amp;<br>Retirement Specialist</h1>
    <p>with a unique approach to financial planning.</p>
  </div>

  <h2 class="abs title" style="left:111px;top:760px">My <span>Specialties</span></h2>

  <div class="abs arrow" style="left:69px"><svg width="14" height="14" viewBox="0 0 14 14"><path d="M9 2 4 7l5 5" fill="none" stroke="#fff" stroke-width="2.4"/></svg></div>
  <div class="abs arrow" style="left:1097px"><svg width="14" height="14" viewBox="0 0 14 14"><path d="m5 2 5 5-5 5" fill="none" stroke="#fff" stroke-width="2.4"/></svg></div>

  <div class="abs card" style="left:111px">
    <div class="ico"><svg width="34" height="34" viewBox="0 0 34 34"><rect x="9" y="5" width="16" height="19" rx="1" fill="#ffc700"/><path d="M4 25q8 6 14 3l10-5" fill="none" stroke="#ffc700" stroke-width="2.5"/></svg></div>
    <h3>Estate planning</h3>
    <p>Ensure your legacy is protected with comprehensive estate planning.</p>
  </div>
  <div class="abs card" style="left:361px">
    <div class="ico"><svg width="34" height="34" viewBox="0 0 34 34"><circle cx="14" cy="10" r="7" fill="#ffc700"/><path d="M8 20h14l4 10M10 20l-3 10M6 30h24" fill="none" stroke="#ffc700" stroke-width="2.5"/></svg></div>
    <h3>Retirement forecasting</h3>
    <p>Plan for a fulfilling retirement with our expert forecasting services.</p>
  </div>
  <div class="abs card on" style="left:612px">
    <div class="ico"><svg width="36" height="36" viewBox="0 0 36 36"><rect x="4" y="12" width="26" height="18" rx="3" fill="#fff"/><circle cx="24" cy="21" r="2.5" fill="#0d0d0d"/><path d="M10 12l10-6 4 6M28 4v6M25 7l3-3 3 3" fill="none" stroke="#fff" stroke-width="2.2"/></svg></div>
    <h3>Final expense</h3>
    <p>Prepare for life's final expenses with peace of mind. My services help you plan for costs..</p>
  </div>
  <div class="abs card" style="left:860px">
    <div class="ico"><svg width="34" height="34" viewBox="0 0 34 34"><path d="M17 3 29 8v9c0 7-5 12-12 14C10 29 5 24 5 17V8z" fill="#ffc700"/><path d="m11 17 4 4 8-8" fill="none" stroke="#fff" stroke-width="2.6"/></svg></div>
    <h3>Life insurance</h3>
    <p>Safeguard your family's future with tailored life insurance solutions.</p>
  </div>

  <div class="abs quote" role="img" aria-label="Gold-toned photo of advisors meeting with clients behind the message">
    <p>You have a lifetime of accomplishments. Learning about them is my extraordinary honor. When I meet clients to make a plan for their final years of work and savings, I understand my solemn privilege. Your capital is irreplaceable. My job is to maximize its benefit for your health, family, and legacy.</p>
  </div>

  <h2 class="abs title" style="left:0;width:1198px;text-align:center;top:1550px">Insurance <span>Offerings</span></h2>

  <div class="abs offer" style="left:148px">
    <svg width="96" height="96" viewBox="0 0 96 96" style="margin-top:18px"><path d="M48 6 68 14v16c0 14-9 22-20 26C37 52 28 44 28 30V14z" fill="none" stroke="#ffc700" stroke-width="3"/><path d="m40 30 6 6 11-14" fill="none" stroke="#ffc700" stroke-width="3"/><path d="M10 50l6 14 14 10v14h10V72L28 58M86 50l-6 14-14 10v14H56V72l12-14" fill="none" stroke="#0d0d0d" stroke-width="3"/></svg>
    <h4>Whole and<br>Universal Life</h4>
  </div>
  <div class="abs offer on" style="left:470px">
    <svg width="82" height="82" viewBox="0 0 82 82" style="margin-top:52px"><rect x="4" y="10" width="62" height="54" rx="3" fill="none" stroke="#0d0d0d" stroke-width="3"/><path d="M4 22h62M20 4v12M50 4v12" stroke="#0d0d0d" stroke-width="3"/><rect x="14" y="30" width="8" height="6" fill="none" stroke="#ffc700" stroke-width="2"/><rect x="28" y="30" width="8" height="6" fill="none" stroke="#ffc700" stroke-width="2"/><rect x="14" y="44" width="8" height="6" fill="none" stroke="#ffc700" stroke-width="2"/><rect x="28" y="44" width="8" height="6" fill="none" stroke="#ffc700" stroke-width="2"/><circle cx="60" cy="58" r="16" fill="#fff" stroke="#ffc700" stroke-width="3"/><text x="60" y="65" text-anchor="middle" font-family="Lato,sans-serif" font-size="20" font-weight="700" fill="#ffc700">$</text></svg>
    <h4 style="margin-top:8px">Annuities</h4>
  </div>
  <div class="abs offer" style="left:800px">
    <svg width="80" height="92" viewBox="0 0 80 92" style="margin-top:28px"><rect x="10" y="4" width="54" height="78" fill="none" stroke="#0d0d0d" stroke-width="3"/><path d="M20 22h34M20 32h34M20 42h34M20 52h24M20 62h20" stroke="#ffc700" stroke-width="2.5"/><circle cx="60" cy="76" r="13" fill="#fff" stroke="#ffc700" stroke-width="3"/><path d="m54 76 5 5 8-9" fill="none" stroke="#ffc700" stroke-width="3"/></svg>
    <h4 style="margin-top:2px">Term and Final<br>Expense</h4>
  </div>

  <h2 class="abs title" style="left:0;width:1200px;text-align:center;top:1927px">Allow Me To <span>Introduce Myself.</span></h2>
  <p class="abs sub" style="top:1982px">(Let’s plan for golden memories.)</p>

  <div class="abs field" style="left:111px;top:2046px;width:317px;height:55px">First Name</div>
  <div class="abs field" style="left:441px;top:2046px;width:317px;height:55px">Email</div>
  <div class="abs field" style="left:771px;top:2046px;width:317px;height:55px">Phone</div>
  <div class="abs field" style="left:111px;top:2115px;width:977px;height:115px">Questions /Comments</div>
  <div class="abs btn">Say Hi...!</div>

  <div class="abs footer"></div>
  <div class="abs foot-brand">Dalton Whitfield</div>
  <div class="abs foot-nav">
    <span style="left:236px">Home</span>
    <span style="left:346px">|</span>
    <span style="left:419px">Specialties</span>
    <span style="left:560px">|</span>
    <span style="left:633px">Insurance Offers</span>
    <span style="left:815px">|</span>
    <span style="left:888px">Contact Us</span>
  </div>
  <div class="abs social" style="left:565px;background:var(--gold)" aria-label="Social link"></div>
  <div class="abs social" style="left:615px;width:22px;height:22px;top:2630px;background:var(--white)" aria-label="Social link"></div>
  <div class="abs bar">© 2024 Dalton Whitfield. All Rights Reserved.</div>

</div>
</body>
</html>
```